Ayurvedic Beauty Company in Need of Business Cards

My company is a high-end ayurvedic beauty brand. I need a business card that represents that. The designer should utilize logo and color palette. I want these cards to be printed with the foil accents so keep that in mind.

I have attached the ai of my logo and business card info. As well as, some of the product we are launching soon, they do not have to be on the card.

Be creative and have fun.

Thanks in advance,

Marla

```html
<!DOCTYPE html>
<html lang="en">
<head>
<meta charset="UTF-8">
<title>Sorvaya Business Cards</title>
<link href="https://fonts.googleapis.com/css2?family=Montserrat:wght@400;500&display=swap" rel="stylesheet">
<style>
  :root {
    --canvas-bg: #ece8e4;
    --plum: #6f1b58;
    --plum-light: #8d3b76;
    --plum-soft: #a2598c;
    --gold: #dcbd84;
    --white: #ffffff;
  }
  * { margin: 0; padding: 0; box-sizing: border-box; }
  html, body {
    width: 1200px;
    height: 950px;
    overflow: hidden;
    background: var(--canvas-bg);
    font-family: "Montserrat", Arial, sans-serif;
  }
  .canvas {
    position: relative;
    width: 1200px;
    height: 950px;
  }
  .card {
    position: absolute;
    left: 240px;
    width: 720px;
    height: 412px;
    background: var(--plum);
    overflow: hidden;
    box-shadow: 0 6px 18px rgba(60, 20, 50, 0.25);
  }
  .card--contact { top: 50px; }
  .card--brand { top: 488px; }

  .card__decor {
    position: absolute;
    inset: 0;
    background: radial-gradient(ellipse at 50% 50%, var(--plum-light) 0%, var(--plum) 55%, var(--plum-soft) 100%);
  }
  .contact {
    position: absolute;
    left: 0; right: 0;
    top: 100px;
    text-align: center;
    color: var(--white);
  }
  .contact__name {
    color: var(--gold);
    font-size: 26px;
    font-weight: 500;
    letter-spacing: 1px;
    text-transform: uppercase;
  }
  .contact__role {
    font-size: 19px;
    margin: 4px 0 14px;
  }
  .contact__line {
    font-size: 18px;
    line-height: 29px;
  }

  .brand {
    position: absolute;
    inset: 0;
    display: flex;
    align-items: center;
    justify-content: center;
    gap: 26px;
  }
  .brand__name {
    color: var(--gold);
    font-size: 30px;
    font-weight: 500;
    letter-spacing: 2px;
    text-transform: uppercase;
  }
  .brand__dot {
    width: 96px;
    height: 96px;
    border-radius: 50%;
    background: var(--gold);
  }
</style>
</head>
<body>
<main class="canvas">
  <section class="card card--contact">
    <div class="card__decor" role="img" aria-label="Large faint brand mark pattern in soft plum tones"></div>
    <div class="contact">
      <p class="contact__name">Marla Vance</p>
      <p class="contact__role">CEO</p>
      <p class="contact__line">Ph. 1(888) 555-0142</p>
      <p class="contact__line">Mob. 1(347) 555-0187</p>
      <p class="contact__line">marla@lovesorvaya.com</p>
      <p class="contact__line">www.lovesorvaya.com</p>
    </div>
  </section>

  <section class="card card--brand">
    <div class="brand">
      <span class="brand__name">Sorvaya</span>
      <span class="brand__dot"></span>
    </div>
  </section>
</main>
</body>
</html>
```